Packaging Design Project for Snack product

we are manufacturer banana chips and potato based snacks.our company name is "velmora Foods" and,looking a packaging design for our new product "Potato Twirlies" under brand name " Munchlo".

we need nice colour scheme and wording on the front and back.just a little more professional looking with the wow factor to help it stand out on the shelve.

so pls find below information about the design:
Company name: Velmora Foods
Brand name : Munchlo
Product name : Potato Twirlies
Flavored : Sweet & Spicy
Package Size : 40 GM and 100 GM

Target Market(s)

Retail Customers

Industry/Entity Type

It Company

Requirements
Must have
• In this design we need small visible part for display our product.

```html
<!DOCTYPE html>
<html lang="en">
<head>
<meta charset="utf-8">
<title>Munchlo Potato Twirlies – Sweet &amp; Spicy Pack Front</title>
<link rel="stylesheet" href="https://fonts.googleapis.com/css2?family=Baloo+2:wght@800&family=Bevan&family=Open+Sans:wght@700;800&display=swap">
<style>
  :root {
    --stage: #e6e6e8;
    --pack-blue: #2e3192;
    --pack-blue-light: #3b3fa6;
    --banner-orange: #e85a27;
    --banner-orange-light: #f07a35;
    --base-yellow: #f7c733;
    --base-orange: #f08a1e;
    --title-red: #d3202a;
    --brand-yellow: #fbd233;
    --brand-orange: #f0891f;
    --ink: #2b2b2b;
    --maker-grey: #3d3d3d;
    --white: #ffffff;
    --chip-light: #f8d796;
    --chip-deep: #e8a24a;
  }
  html, body {
    margin: 0;
    padding: 0;
    width: 1200px;
    height: 1000px;
    overflow: hidden;
    background: var(--stage);
  }
  .canvas {
    position: relative;
    width: 1200px;
    height: 1000px;
    display: flex;
    align-items: center;
    justify-content: center;
  }
  .pack-front {
    width: 1000px;
    height: 800px;
    display: block;
    border-radius: 10px;
    box-shadow: 0 10px 30px rgba(0, 0, 0, 0.18);
  }
  .brand-name {
    font-family: "Baloo 2", sans-serif;
    font-weight: 800;
    font-style: italic;
    font-size: 112px;
  }
  .product-name {
    font-family: "Bevan", serif;
    fill: var(--title-red);
    stroke: var(--white);
    stroke-width: 9px;
    stroke-linejoin: round;
    paint-order: stroke fill;
  }
  .product-name__first { font-size: 100px; }
  .product-name__second { font-size: 86px; }
  .flavour {
    font-family: "Open Sans", sans-serif;
    font-weight: 800;
    font-size: 42px;
    fill: var(--ink);
  }
  .flavour-amp { fill: var(--title-red); font-size: 50px; }
  .maker-name {
    font-family: "Open Sans", sans-serif;
    font-weight: 700;
    font-size: 34px;
    fill: var(--maker-grey);
  }
  .maker-mark { fill: var(--maker-grey); }
  .net-weight {
    font-family: "Open Sans", sans-serif;
    font-weight: 700;
    font-size: 26px;
    fill: var(--ink);
  }
</style>
</head>
<body>
<main class="canvas">
  <svg class="pack-front" viewBox="0 0 1000 800" xmlns="http://www.w3.org/2000/svg" aria-labelledby="pack-title">
    <title id="pack-title">Munchlo Potato Twirlies, sweet and spicy, by Velmora Foods, 100 gm</title>
    <defs>
      <linearGradient id="base-gradient" x1="0" y1="0" x2="0" y2="1">
        <stop offset="0" stop-color="var(--base-yellow)"/>
        <stop offset="1" stop-color="var(--base-orange)"/>
      </linearGradient>
      <linearGradient id="banner-gradient" x1="0" y1="0" x2="1" y2="1">
        <stop offset="0" stop-color="var(--banner-orange-light)"/>
        <stop offset="1" stop-color="var(--banner-orange)"/>
      </linearGradient>
      <linearGradient id="brand-gradient" x1="0" y1="0" x2="0" y2="1">
        <stop offset="0" stop-color="var(--brand-yellow)"/>
        <stop offset="1" stop-color="var(--brand-orange)"/>
      </linearGradient>
      <radialGradient id="window-gradient" cx="0.45" cy="0.55" r="0.7">
        <stop offset="0" stop-color="var(--chip-light)"/>
        <stop offset="1" stop-color="var(--chip-deep)"/>
      </radialGradient>
    </defs>

    <!-- pack body -->
    <rect class="pack-top" x="0" y="0" width="1000" height="800" fill="var(--pack-blue)"/>
    <rect class="pack-seal" x="0" y="0" width="1000" height="40" fill="var(--pack-blue-light)"/>

    <!-- warm lower field -->
    <path class="pack-base" d="M0 420 C320 400 680 330 1000 250 L1000 800 L0 800 Z" fill="url(#base-gradient)"/>

    <!-- tilted title banner -->
    <path class="title-banner" d="M40 300 L950 110 L985 345 L90 575 Z" fill="url(#banner-gradient)"/>

    <!-- product window -->
    <g class="product-window" role="img" aria-label="Clear window showing the golden potato snacks inside">
      <path d="M110 785 C100 650 190 520 330 470 C450 430 560 440 610 470 C600 560 580 620 560 650 C470 710 300 765 110 785 Z" fill="url(#window-gradient)" stroke="var(--banner-orange)" stroke-width="6"/>
    </g>

    <!-- lower blue wave -->
    <path class="base-wave" d="M360 800 C540 720 760 650 1000 600 L1000 690 C820 720 650 765 540 800 Z" fill="var(--pack-blue)"/>

    <!-- brand -->
    <text class="brand-name" x="70" y="250" fill="url(#brand-gradient)" transform="rotate(-12 70 250)">Munchlo</text>

    <!-- product name, one line along the banner -->
    <text class="product-name" x="100" y="465" transform="rotate(-12 100 465)"><tspan class="product-name__first">Potato</tspan> <tspan class="product-name__second">Twirlies</tspan></text>

    <!-- flavour -->
    <text class="flavour" x="640" y="440">sweet<tspan class="flavour-amp">&amp;</tspan>spicy</text>

    <!-- maker -->
    <g class="maker">
      <circle class="maker-mark" cx="665" cy="522" r="14"/>
      <text class="maker-name" x="690" y="534">Velmora Foods</text>
    </g>

    <!-- net weight -->
    <text class="net-weight" x="800" y="755">100 gm</text>
  </svg>
</main>
</body>
</html>
```